Marlow Pike PPT 1

I need a PPT template that I could apply to several uses both internally and externally.
Marlow Pike is not a new company but rather a new spin-off from my previous brand. We are a Business Consulting firm known for our ability implement the advice we provide our clients and see it through to fruition. The vast majority of our projects involve IT or software technology. Particularly with new software implementations, software integrations arising from a merger or acquisition. We consult to almost every industry except Mining, construction and agriculture but mostly for Financial Services, automotive and Hospitality services. We offer a tailored service through trusted, longstanding relationships with our clients.
From a look, feel and overall theme perspective, Pike is the Viking god of war but, more importantly, he is known for his WISDOM, ADAPATABILITY, RESILENCE. He is in fact a shape shifter. We chose Pike because we advise our clients on ways to remain Agile and adaptable to rapidly changing environments to remain competitive now and in the future.
The word steel was added to denote strength, reliability sustainability.
I have recently run a logo design competition for the new logo.

I would like an all-purpose PPT template that is crisp, clean, uncomplicated but professional and attractive to the eye.
I am keen to see some ideas.
Thanks
Dana

```html
<!DOCTYPE html>
<html lang="en">
<head>
<meta charset="utf-8">
<title>Marlow Pike – Presentation Template</title>
<link rel="stylesheet" href="https://fonts.googleapis.com/css2?family=Montserrat:wght@400;500;600;700;800&family=Oswald:wght@500;600&display=swap">
<style>
:root{
  --red:#d3141b;
  --ink:#1f1f1f;
  --steel:#7d7d7d;
  --steel-light:#b5b5b5;
  --mist:#ececec;
  --paper:#ffffff;
  --board:#d9dadb;
  --night:#2b2b2b;
}
*{box-sizing:border-box;margin:0;padding:0}
html,body{width:900px;height:1200px;overflow:hidden;background:var(--board)}
body{position:relative;font-family:"Montserrat",Arial,sans-serif;color:var(--ink)}
.slide{position:absolute;width:270px;height:152px;background:var(--paper);overflow:hidden;box-shadow:0 1px 3px rgba(0,0,0,.18)}
.c1{left:33px}.c2{left:315px}.c3{left:597px}
.r1{top:27px}.r2{top:193px}.r3{top:360px}.r4{top:526px}.r5{top:693px}.r6{top:857px}.r7{top:1021px}
.abs{position:absolute}
.title{position:absolute;left:10px;top:8px;font-size:9px;font-weight:700;letter-spacing:.1px}
.title::after{content:"";position:absolute;left:0;top:14px;width:14px;height:1.5px;background:var(--steel);box-shadow:15px 0 0 -0px var(--red);clip-path:inset(0 -5px 0 0)}
.title .dots{display:none}
.brand{position:absolute;right:8px;top:7px;font-size:5.5px;font-weight:700;color:var(--steel);display:flex;align-items:center;gap:2px;letter-spacing:.3px;text-transform:uppercase}
.brand i{display:block;width:4px;height:4px;border-radius:50%;background:var(--red)}
.foot{position:absolute;left:8px;right:8px;bottom:7px;height:4px}
.foot::before{content:"";position:absolute;left:0;top:0;width:4px;height:4px;border-radius:50%;background:var(--red)}
.foot::after{content:"";position:absolute;left:8px;right:8px;top:2px;height:.4px;background:var(--steel-light)}
.foot span{position:absolute;right:0;top:-1px;font-size:3px;color:var(--steel)}
.fine{font-size:3.3px;line-height:1.35;color:#777}
.h6{font-size:5px;font-weight:700;color:var(--ink)}
.red{color:var(--red)}
.photo{position:absolute;background:linear-gradient(135deg,#9a9a9a,#5c5c5c)}
.photo.dark{background:linear-gradient(135deg,#4a4a4a,#1e1e1e)}
.photo.light{background:linear-gradient(135deg,#d5d5d5,#8d8d8d)}
.dot-icon{position:absolute;width:15px;height:15px;border-radius:50%;background:var(--red);border:2px solid #f3c9cb}
.dot-icon::after{content:"";position:absolute;left:4px;top:4px;width:3px;height:3px;border:1px solid #fff;border-radius:50%}
.map{position:absolute;background:radial-gradient(ellipse at center,#f1f1f1 0%,#f7f7f7 60%,transparent 75%)}
</style>
</head>
<body>

<!-- Row 1 -->
<section class="slide c1 r1" style="background:var(--night)">
  <div class="photo dark" style="inset:0;opacity:.9" role="img" aria-label="Dim office photo with people at work"></div>
  <div class="abs" style="left:48px;top:44px;font-size:24px;font-weight:700;color:#cfcfcf;letter-spacing:1px;display:flex;align-items:center;gap:6px"><i style="display:block;width:12px;height:12px;border-radius:50%;background:var(--red)"></i>MARLOW PIKE</div>
  <div class="abs" style="left:128px;top:96px;width:142px;height:9px;background:#666;color:#fff;font-size:6.2px;font-weight:600;padding:1px 0 0 6px">COMPANY BUSINESS MARKETING</div>
  <div class="abs" style="left:152px;top:109px;font-size:4.5px;color:#ddd;letter-spacing:1.5px">www.<span class="red">website</span>.com</div>
</section>

<section class="slide c2 r1">
  <div class="abs" style="left:6px;top:5px;width:6px;height:6px;background:var(--red)"></div>
  <div class="abs" style="left:18px;top:22px;font-size:10px;font-weight:700;color:#8a8a8a;display:flex;align-items:center;gap:3px"><i style="display:block;width:6px;height:6px;border-radius:50%;background:var(--red)"></i>MARLOW PIKE</div>
  <div class="abs" style="left:15px;top:66px;font-family:Oswald,sans-serif;font-size:20px;font-weight:600;color:#555;line-height:1">BUSINESS</div>
  <div class="abs" style="left:15px;top:88px;font-size:10px;font-weight:700;color:var(--red)">MARKETING</div>
  <div class="abs" style="left:15px;top:102px;width:16px;height:1.5px;background:var(--red)"></div>
  <div class="abs" style="left:15px;top:110px;font-size:6px;font-style:italic;color:#666">Presentation</div>
  <div class="abs fine" style="left:15px;top:119px;width:75px">Short line of opening copy for the title slide.</div>
  <div class="abs" style="left:17px;top:138px;display:flex;gap:3px"><i style="width:3px;height:3px;border-radius:50%;background:#777;display:block"></i><i style="width:3px;height:3px;border-radius:50%;background:var(--red);display:block"></i><i style="width:3px;height:3px;border-radius:50%;background:#777;display:block"></i></div>
  <div class="photo light" style="left:114px;top:0;width:156px;height:123px" role="img" aria-label="Business person holding a tablet with consulting icons"></div>
  <div class="abs" style="left:114px;top:123px;width:156px;height:29px;background:#2a2a2a;color:#fff;font-size:4.8px;letter-spacing:1.8px;text-align:center;padding-top:12px">WWW.<span class="red">WEBSITE</span>.COM</div>
</section>

<section class="slide c3 r1">
  <div class="brand"><i></i>Marlow Pike</div>
  <div class="abs" style="left:45px;top:67px;font-size:14px;font-weight:700">Agenda</div>
  <div class="abs" style="left:119px;top:30px;width:110px">
    <div class="h6"><span class="red">1.</span> Lorem ipsum</div><div class="fine" style="margin:1px 0 8px 7px">Brief agenda point description goes here for this item.</div>
    <div class="h6"><span class="red">2.</span> Lorem ipsum</div><div class="fine" style="margin:1px 0 8px 7px">Brief agenda point description goes here for this item.</div>
    <div class="h6"><span class="red">3.</span> Lorem ipsum</div><div class="fine" style="margin:1px 0 8px 7px">Brief agenda point description goes here for this item.</div>
    <div class="h6"><span class="red">4.</span> Lorem ipsum</div><div class="fine" style="margin:1px 0 0 7px">Brief agenda point description goes here for this item.</div>
  </div>
  <div class="foot"><span>2</span></div>
</section>

<!-- Row 2 -->
<section class="slide c1 r2">
  <div class="title">Text Added Hare</div><div class="brand"><i></i>Marlow Pike</div>
  <div class="abs" style="left:30px;top:35px;width:130px">
    <div class="h6" style="font-size:4.3px">01. Aliquam Erat Volutpat</div><div class="fine" style="margin:1px 0 6px 8px">Short supporting line for this numbered point.</div>
    <div class="h6" style="font-size:4.3px">02. Consectetuer Adipiscing Elit</div><div class="fine" style="margin:1px 0 6px 8px">Short supporting line for this numbered point.</div>
    <div class="h6" style="font-size:4.3px">03. Duis Autem Vel Eum</div><div class="fine" style="margin:1px 0 6px 8px">Short supporting line for this numbered point.</div>
    <div class="h6" style="font-size:4.3px">04. Aliquam Erat Volutpat</div><div class="fine" style="margin:1px 0 0 8px">Short supporting line for this numbered point.</div>
  </div>
  <div class="abs" style="left:147px;top:31px;width:93px;height:88px;background:linear-gradient(90deg,#5a5a5a,#b0b0b0)"></div>
  <div class="dot-icon" style="left:137px;top:37px"></div><div class="dot-icon" style="left:137px;top:65px"></div><div class="dot-icon" style="left:137px;top:94px"></div>
  <div class="abs" style="left:163px;top:38px;width:72px;color:#fff">
    <div style="font-size:5px;font-weight:600">Lorem Ipsum</div><div style="font-size:3.2px;margin:1px 0 12px">Short panel caption line here.</div>
    <div style="font-size:5px;font-weight:600">Lorem Ipsum</div><div style="font-size:3.2px;margin:1px 0 13px">Short panel caption line here.</div>
    <div style="font-size:5px;font-weight:600">Lorem Ipsum</div><div style="font-size:3.2px;margin-top:1px">Short panel caption line here.</div>
  </div>
  <div class="foot"><span>3</span></div>
</section>

<section class="slide c2 r2">
  <div class="title">Text Added Hare</div><div class="brand"><i></i>Marlow Pike</div>
  <div class="map" style="left:30px;top:22px;width:210px;height:100px" role="img" aria-label="Faint world map"></div>
  <svg class="abs" style="left:0;top:0" width="270" height="152">
    <g fill="none" stroke="#2a2a2a" stroke-width="1.6">
      <rect x="50" y="35" width="44" height="68" rx="5"/>
      <rect x="112" y="35" width="44" height="68" rx="5"/>
      <rect x="174" y="35" width="44" height="68" rx="5"/>
      <path d="M94 88 H112 M156 50 H174"/>
    </g>
    <g fill="none" stroke="#333" stroke-width=".8">
      <circle cx="72" cy="46" r="3"/><path d="M71 50h2"/>
      <rect x="130" y="44" width="8" height="6"/><path d="M130 44l4 3 4-3"/>
      <path d="M192 50l3-3 2 2 4-4 M192 44v7h9"/>
    </g>
    <g font-family="Montserrat" font-size="4.5" font-weight="700" fill="#d3141b" text-anchor="middle">
      <text x="72" y="58">IDEA</text><text x="134" y="58">PROMOTION</text><text x="196" y="58">GROWTH</text>
    </g>
  </svg>
  <div class="abs fine" style="left:53px;top:62px;width:38px;text-align:center;font-size:2.9px">Brief note on how ideas are shaped into plans.</div>
  <div class="abs fine" style="left:115px;top:62px;width:38px;text-align:center;font-size:2.9px">Brief note on how the plan reaches the market.</div>
  <div class="abs fine" style="left:177px;top:62px;width:38px;text-align:center;font-size:2.9px">Brief note on how results grow over time.</div>
  <div class="abs fine" style="left:32px;top:114px;width:206px;text-align:center">A short closing paragraph summarising the three stages, from first idea through promotion to lasting growth for the client.</div>
  <div class="foot"><span>4</span></div>
</section>

<section class="slide c3 r2">
  <div class="brand"><i></i>Marlow Pike</div>
  <div class="abs" style="left:12px;top:11px;font-size:8px;font-weight:700;line-height:1.2">Lorem Ipsum<br>Dolor Sit<br>Ametkeeper.</div>
  <div class="abs" style="left:12px;top:49px;width:10px;height:1.5px;background:var(--red)"></div>
  <div class="abs fine" style="left:12px;top:55px;width:80px;text-align:justify">A short introductory paragraph that explains the purpose of this slide and the value it brings.<br><br>A second paragraph adds supporting detail about the approach, the team and the expected results.<br><br>A closing line sums it up.</div>
  <div class="photo" style="left:94px;top:22px;width:176px;height:72px" role="img" aria-label="Hand pressing a consulting network diagram"></div>
  <div class="abs" style="left:122px;top:76px;width:48px;height:78px;background:#fff;box-shadow:0 0 2px rgba(0,0,0,.25)"></div>
  <div class="abs" style="left:187px;top:76px;width:48px;height:78px;background:#fff;box-shadow:0 0 2px rgba(0,0,0,.25)"></div>
  <div class="abs" style="left:122px;top:76px;width:48px;height:14px;background:var(--red);color:#fff;font-size:6.5px;font-weight:700;text-align:center;padding-top:3px">Text Here</div>
  <div class="abs" style="left:187px;top:76px;width:48px;height:14px;background:var(--red);color:#fff;font-size:6.5px;font-weight:700;text-align:center;padding-top:3px">Text Here</div>
  <div class="abs fine" style="left:126px;top:94px;width:40px;font-size:2.8px">Short card copy describing this point in a few brief words.</div>
  <div class="abs fine" style="left:191px;top:94px;width:40px;font-size:2.8px">Short card copy describing this point in a few brief words.</div>
  <div class="foot"><span>5</span></div>
</section>

<!-- Row 3 -->
<section class="slide c1 r3">
  <div class="title">Text Added Hare</div><div class="brand"><i></i>Marlow Pike</div>
  <div class="abs fine" style="left:15px;top:30px;width:40px;font-size:3.6px">A short paragraph introducing the team and its values.<br><br>A second short paragraph on how the team works with each client, day by day.</div>
  <div class="photo" style="left:62px;top:18px;width:90px;height:118px;clip-path:polygon(40% 0,100% 0,60% 100%,0 100%)" role="img" aria-label="Person standing by office windows"></div>
  <div class="dot-icon" style="left:138px;top:32px;background:#fff;border-color:#ddd"></div>
  <div class="dot-icon" style="left:125px;top:68px;background:#fff;border-color:#ddd"></div>
  <div class="dot-icon" style="left:112px;top:104px;background:#fff;border-color:#ddd"></div>
  <div class="abs" style="left:166px;top:35px;width:90px"><div class="h6">We Before Me</div><div class="fine" style="margin-top:1px">Short line about putting the team first.</div></div>
  <div class="abs" style="left:152px;top:71px;width:100px"><div class="h6">We Are Good People</div><div class="fine" style="margin-top:1px">Short line about honesty and trust.</div></div>
  <div class="abs" style="left:139px;top:107px;width:100px"><div class="h6">We Work with Heart</div><div class="fine" style="margin-top:1px">Short line about care for every client.</div></div>
  <div class="foot"><span>6</span></div>
</section>

<section class="slide c2 r3">
  <div class="photo dark" style="left:12px;top:10px;width:246px;height:132px;background:linear-gradient(135deg,#3e3e3e,#262626)" role="img" aria-label="Dim photo of a business meeting"></div>
  <div class="abs" style="left:85px;top:70px;width:16px;height:16px;border-radius:50%;background:var(--red)"></div>
  <div class="abs" style="left:136px;top:50px;font-size:17px;font-weight:600;color:#fff;line-height:1">Section</div>
  <div class="abs" style="left:136px;top:67px;font-size:17px;font-weight:800;color:var(--red);line-height:1">Break</div>
  <div class="abs" style="left:136px;top:89px;width:100px;font-size:5px;color:#ddd;line-height:1.3">Lorem ipsum dolor sit amet, consectetuer sed diam nonummy euismod tincid</div>
</section>

<section class="slide c3 r3">
  <div class="title">Text Added Hare</div><div class="brand"><i></i>Marlow Pike</div>
  <div class="photo light" style="left:24px;top:32px;width:98px;height:97px" role="img" aria-label="Two colleagues talking at a laptop"></div>
  <div class="abs" style="left:50px;top:116px;width:64px;height:12px;background:var(--red);color:#fff;font-size:6.5px;font-weight:700;text-align:center;padding-top:2px">Service</div>
  <div class="dot-icon" style="left:133px;top:39px"></div><div class="dot-icon" style="left:133px;top:71px"></div><div class="dot-icon" style="left:133px;top:104px"></div>
  <div class="abs" style="left:158px;top:38px;width:80px">
    <div class="h6">Project name</div><div class="fine" style="margin:1px 0 18px">Short line about this project and its outcome.</div>
    <div class="h6">Project name</div><div class="fine" style="margin:1px 0 18px">Short line about this project and its outcome.</div>
    <div class="h6">Project name</div><div class="fine" style="margin-top:1px">Short line about this project and its outcome.</div>
  </div>
  <div class="foot"><span>8</span></div>
</section>

<!-- Row 4 -->
<section class="slide c1 r4">
  <div class="brand"><i></i>Marlow Pike</div>
  <div class="abs" style="left:12px;top:10px;font-size:9px;font-weight:700;line-height:1.25">Market<br>Opportunities.</div>
  <div class="abs" style="left:12px;top:39px;width:10px;height:1.5px;background:var(--red)"></div>
  <div class="abs" style="left:0;top:45px;width:94px;height:77px;background:var(--mist)"></div>
  <div class="abs" style="left:14px;top:52px;width:76px">
    <div class="h6"><span class="red">●</span> Lorem Ipsum</div><div class="fine" style="margin:1px 0 6px 6px">Short note on this opportunity.</div>
    <div class="h6"><span class="red">●</span> Lorem Ipsum</div><div class="fine" style="margin:1px 0 6px 6px">Short note on this opportunity.</div>
    <div class="h6"><span class="red">●</span> Lorem Ipsum</div><div class="fine" style="margin:1px 0 0 6px">Short note on this opportunity.</div>
  </div>
  <svg class="abs" style="left:100px;top:30px" width="165" height="115" font-family="Montserrat" font-size="3.5" fill="#555" text-anchor="middle">
    <line x1="5" y1="88" x2="160" y2="88" stroke="#ccc" stroke-width=".4"/>
    <g transform="translate(0,88)">
      <rect x="42" y="-43" width="4" height="43" fill="#2a2a2a"/><rect x="50" y="-24" width="4" height="24" fill="#a0a0a0"/><rect x="58" y="-20" width="4" height="20" fill="#d3141b"/>
      <rect x="82" y="-44" width="4" height="44" fill="#2a2a2a" transform="translate(0,0)"/>
    </g>
    <g transform="translate(0,88)">
      <rect x="82" y="-25" width="4" height="25" fill="#2a2a2a"/><rect x="90" y="-44" width="4" height="44" fill="#a0a0a0"/><rect x="98" y="-20" width="4" height="20" fill="#d3141b"/>
      <rect x="122" y="-35" width="4" height="35" fill="#2a2a2a"/><rect x="130" y="-18" width="4" height="18" fill="#a0a0a0"/><rect x="138" y="-30" width="4" height="30" fill="#d3141b"/>
    </g>
    <g transform="translate(0,88)">
      <rect x="10" y="-43" width="4" height="43" fill="#2a2a2a"/><rect x="18" y="-24" width="4" height="24" fill="#a0a0a0"/><rect x="26" y="-20" width="4" height="20" fill="#d3141b"/>
    </g>
    <text x="12" y="43">43%</text><text x="20" y="62">24%</text><text x="28" y="66">20%</text>
    <text x="84" y="62">25%</text><text x="92" y="42">44%</text><text x="100" y="66">20%</text>
    <text x="124" y="51">35%</text><text x="132" y="68">18%</text><text x="140" y="56">30%</text>
  </svg>
  <div class="abs" style="left:100px;top:30px;width:165px;height:115px">
    <svg width="165" height="115" font-family="Montserrat" font-size="3.5" fill="#555" text-anchor="middle">
      <rect x="42" y="0" width="0" height="0"/>
    </svg>
  </div>
  <svg class="abs" style="left:100px;top:30px" width="165" height="115" font-family="Montserrat" font-size="3.5" fill="#555" text-anchor="middle">
    <rect x="0" y="0" width="165" height="115" fill="#fff"/>
    <line x1="5" y1="88" x2="160" y2="88" stroke="#ccc" stroke-width=".4"/>
    <rect x="44" y="45" width="4" height="43" fill="#2a2a2a"/><rect x="50" y="64" width="4" height="24" fill="#a0a0a0"/><rect x="56" y="68" width="4" height="20" fill="#d3141b"/>
    <rect x="84" y="63" width="4" height="25" fill="#2a2a2a"/><rect x="90" y="44" width="4" height="44" fill="#a0a0a0"/><rect x="96" y="68" width="4" height="20" fill="#d3141b"/>
    <rect x="124" y="53" width="4" height="35" fill="#2a2a2a"/><rect x="130" y="70" width="4" height="18" fill="#a0a0a0"/><rect x="136" y="58" width="4" height="30" fill="#d3141b"/>
    <rect x="10" y="15" width="4" height="73" fill="#2a2a2a"/>
    <text x="12" y="13">43%</text>
  </svg>
  <svg class="abs" style="left:100px;top:22px" width="165" height="123" font-family="Montserrat" font-size="3.5" fill="#555" text-anchor="middle">
    <rect width="165" height="123" fill="#fff"/>
    <line x1="5" y1="95" x2="162" y2="95" stroke="#ccc" stroke-width=".4"/>
    <rect x="40" y="24" width="4" height="71" fill="#2a2a2a"/><rect x="47" y="55" width="4" height="40" fill="#a0a0a0"/><rect x="54" y="62" width="4" height="33" fill="#d3141b"/>
    <rect x="80" y="55" width="4" height="40" fill="#2a2a2a"/><rect x="87" y="22" width="4" height="73" fill="#a0a0a0"/><rect x="94" y="62" width="4" height="33" fill="#d3141b"/>
    <rect x="120" y="37" width="4" height="58" fill="#2a2a2a"/><rect x="127" y="65" width="4" height="30" fill="#a0a0a0"/><rect x="134" y="45" width="4" height="50" fill="#d3141b"/>
    <rect x="146" y="20" width="4" height="75" fill="#2a2a2a"/><rect x="153" y="49" width="4" height="46" fill="#a0a0a0"/><rect x="160" y="12" width="4" height="83" fill="#d3141b"/>
    <text x="42" y="22">43%</text><text x="49" y="53">24%</text><text x="56" y="60">20%</text>
    <text x="82" y="53">25%</text><text x="89" y="20">44%</text><text x="96" y="60">20%</text>
    <text x="122" y="35">35%</text><text x="129" y="63">18%</text><text x="136" y="43">30%</text>
    <text x="148" y="18">45%</text><text x="155" y="47">28%</text><text x="160" y="10">50%</text>
    <text x="49" y="102">1</text><text x="89" y="102">2</text><text x="129" y="102">3</text><text x="155" y="102">4</text>
    <g font-size="3"><rect x="58" y="108" width="2" height="2" fill="#2a2a2a"/><text x="66" y="110">Series1</text><rect x="76" y="108" width="2" height="2" fill="#a0a0a0"/><text x="84" y="110">Series2</text><rect x="94" y="108" width="2" height="2" fill="#d3141b"/><text x="102" y="110">Series3</text></g>
  </svg>
  <div class="foot"><span>9</span></div>
</section>

<section class="slide c2 r4">
  <div class="title">Text Added Hare</div><div class="brand"><i></i>Marlow Pike</div>
  <div class="map" style="left:30px;top:22px;width:210px;height:110px" role="img" aria-label="Faint world map"></div>
  <div class="abs" style="left:32px;top:42px;width:212px;display:flex;gap:8px">
    <div style="flex:1;height:62px;border:1px solid #444;padding:16px 3px 0"><div class="h6" style="font-size:4.2px">Lorem ipsum</div><div class="fine" style="font-size:2.8px;margin-top:1px">Short box copy for this point goes here in brief.</div></div>
    <div style="flex:1;height:62px;border:1px solid #444;padding:16px 3px 0"><div class="h6" style="font-size:4.2px">Lorem ipsum</div><div class="fine" style="font-size:2.8px;margin-top:1px">Short box copy for this point goes here in brief.</div></div>
    <div style="flex:1;height:62px;border:1px solid #444;padding:16px 3px 0"><div class="h6" style="font-size:4.2px">Lorem ipsum</div><div class="fine" style="font-size:2.8px;margin-top:1px">Short box copy for this point goes here in brief.</div></div>
    <div style="flex:1;height:62px;border:1px solid #444;padding:16px 3px 0"><div class="h6" style="font-size:4.2px">Lorem ipsum</div><div class="fine" style="font-size:2.8px;margin-top:1px">Short box copy for this point goes here in brief.</div></div>
  </div>
  <div class="dot-icon" style="left:46px;top:33px"></div><div class="dot-icon" style="left:99px;top:33px"></div><div class="dot-icon" style="left:152px;top:33px"></div><div class="dot-icon" style="left:205px;top:33px"></div>
  <div class="abs" style="left:33px;top:111px;font-size:9px;font-weight:700">+ 35k</div>
  <div class="abs fine" style="left:33px;top:123px;width:170px">A short summary line explaining what this headline figure measures.</div>
  <div class="foot"><span>10</span></div>
</section>

<section class="slide c3 r4">
  <div class="title">Text Added Hare</div><div class="brand"><i></i>Marlow Pike</div>
  <div class="abs" style="left:20px;top:37px;width:240px;display:grid;grid-template-columns:repeat(3,1fr);column-gap:8px;row-gap:10px">
    <div><div class="h6" style="font-size:4.3px"><span class="red">1.</span> Text Added Here</div><div class="fine" style="font-size:2.8px;margin-top:2px">Short column copy about this topic, two or three brief lines of supporting detail.</div></div>
    <div><div class="h6" style="font-size:4.3px"><span class="red">2.</span> Text Added Here</div><div class="fine" style="font-size:2.8px;margin-top:2px">Short column copy about this topic, two or three brief lines of supporting detail.</div></div>
    <div><div class="h6" style="font-size:4.3px"><span class="red">3.</span> Text Added Here</div><div class="fine" style="font-size:2.8px;margin-top:2px">Short column copy about this topic, two or three brief lines of supporting detail.</div></div>
    <div><div class="h6" style="font-size:4.3px"><span class="red">4.</span> Text Added Here</div><div class="fine" style="font-size:2.8px;margin-top:2px">Short column copy about this topic, two or three brief lines of supporting detail.</div></div>
    <div><div class="h6" style="font-size:4.3px"><span class="red">5.</span> Text Added Here</div><div class="fine" style="font-size:2.8px;margin-top:2px">Short column copy about this topic, two or three brief lines of supporting detail.</div></div>
    <div><div class="h6" style="font-size:4.3px"><span class="red">6.</span> Text Added Here</div><div class="fine" style="font-size:2.8px;margin-top:2px">Short column copy about this topic, two or three brief lines of supporting detail.</div></div>
  </div>
  <div class="foot"><span>11</span></div>
</section>

<!-- Row 5 -->
<section class="slide c1 r5">
  <div class="title">Text Added Hare</div><div class="brand"><i></i>Marlow Pike</div>
  <svg class="abs" style="left:14px;top:66px" width="30" height="34"><path d="M2 2h12l12 15-12 15H2l12-15z" fill="#e6e6e6"/></svg>
  <div class="photo" style="left:61px;top:33px;width:51px;height:60px" role="img" aria-label="Colleagues reviewing documents"></div>
  <div class="photo" style="left:127px;top:33px;width:51px;height:60px" role="img" aria-label="Team meeting around a table"></div>
  <div class="photo light" style="left:193px;top:33px;width:51px;height:60px" role="img" aria-label="Charts and tablet on a desk"></div>
  <div class="abs" style="left:61px;top:93px;width:51px;height:1.5px;background:var(--red)"></div>
  <div class="abs" style="left:127px;top:93px;width:51px;height:1.5px;background:var(--red)"></div>
  <div class="abs" style="left:193px;top:93px;width:51px;height:1.5px;background:var(--red)"></div>
  <div class="abs" style="left:61px;top:98px;width:51px"><div class="h6" style="font-size:4.3px;font-weight:500">First <b>Option</b></div><div class="fine" style="font-size:2.8px;margin-top:2px">Short description of the first option in brief.</div></div>
  <div class="abs" style="left:127px;top:98px;width:51px"><div class="h6" style="font-size:4.3px;font-weight:500">Second <b>Option</b></div><div class="fine" style="font-size:2.8px;margin-top:2px">Short description of the second option in brief.</div></div>
  <div class="abs" style="left:193px;top:98px;width:51px"><div class="h6" style="font-size:4.3px;font-weight:500">Third <b>Option</b></div><div class="fine" style="font-size:2.8px;margin-top:2px">Short description of the third option in brief.</div></div>
  <div class="foot"><span>12</span></div>
</section>

<section class="slide c2 r5">
  <div class="title">Text Added Hare</div><div class="brand"><i></i>Marlow Pike</div>
  <svg class="abs" style="left:0;top:0" width="270" height="152">
    <circle cx="62" cy="79" r="33" fill="#eee"/>
    <circle cx="62" cy="79" r="29" fill="#2a2a2a"/>
    <circle cx="62" cy="79" r="25" fill="#8a8a8a"/>
    <path d="M95 72 L108 56 H130 M95 79 H130 M95 86 L108 101 H130" fill="none" stroke="#333" stroke-width=".7"/>
    <text x="62" y="77" text-anchor="middle" font-family="Oswald" font-weight="600" font-size="8" fill="#fff">ADDED</text>
    <text x="62" y="88" text-anchor="middle" font-family="Oswald" font-weight="600" font-size="8" fill="#fff">TEXT HARE</text>
  </svg>
  <div class="dot-icon" style="left:134px;top:49px;width:18px;height:18px"></div>
  <div class="dot-icon" style="left:134px;top:72px;width:18px;height:18px"></div>
  <div class="dot-icon" style="left:134px;top:95px;width:18px;height:18px"></div>
  <div class="abs" style="left:163px;top:50px;width:85px">
    <div class="h6">Project name</div><div class="fine" style="margin:1px 0 11px">Short line about this project and its outcome.</div>
    <div class="h6">Project name</div><div class="fine" style="margin:1px 0 11px">Short line about this project and its outcome.</div>
    <div class="h6">Project name</div><div class="fine" style="margin-top:1px">Short line about this project and its outcome.</div>
  </div>
  <div class="foot"><span>13</span></div>
</section>

<section class="slide c3 r5">
  <div class="title">Text Added Hare</div><div class="brand"><i></i>Marlow Pike</div>
  <div class="abs fine" style="left:14px;top:34px;width:240px">A short introduction explaining the three key figures below and what each one measures across the current reporting period.</div>
  <svg class="abs" style="left:0;top:54px" width="270" height="70" font-family="Montserrat" font-weight="600" font-size="10" text-anchor="middle">
    <g transform="translate(61,32)"><circle r="22" fill="none" stroke="#eee" stroke-width="2.5"/><circle r="22" fill="none" stroke="#2a2a2a" stroke-width="2.5" stroke-dasharray="69.1 138.2" transform="rotate(-90)"/><text y="4" fill="#222">50%</text></g>
    <g transform="translate(132,32)"><circle r="22" fill="none" stroke="#eee" stroke-width="2.5"/><circle r="22" fill="none" stroke="#8a8a8a" stroke-width="2.5" stroke-dasharray="103.7 138.2" transform="rotate(-90)"/><text y="4" fill="#222">75%</text></g>
    <g transform="translate(203,32)"><circle r="22" fill="none" stroke="#eee" stroke-width="2.5"/><circle r="22" fill="none" stroke="#d3141b" stroke-width="2.5" stroke-dasharray="55.3 138.2" transform="rotate(-90)"/><text y="4" fill="#222">40%</text></g>
  </svg>
  <div class="abs fine" style="left:31px;top:123px;width:60px;text-align:center">Short caption for this figure</div>
  <div class="abs fine" style="left:102px;top:123px;width:60px;text-align:center">Short caption for this figure</div>
  <div class="abs fine" style="left:173px;top:123px;width:60px;text-align:center">Short caption for this figure</div>
  <div class="foot"><span>14</span></div>
</section>

<!-- Row 6 -->
<section class="slide c1 r6">
  <div class="title">Text Added Hare</div><div class="brand"><i></i>Marlow Pike</div>
  <svg class="abs" style="left:0;top:0" width="270" height="152" font-family="Montserrat" font-size="4" font-weight="600" text-anchor="middle">
    <polygon points="28,77 53,77 49,84 24,84" fill="#4a4a4a"/>
    <polygon points="56,77 113,77 109,84 52,84" fill="#d3141b"/>
    <polygon points="116,77 140,77 136,84 112,84" fill="#4a4a4a"/>
    <polygon points="143,77 202,77 198,84 139,84" fill="#d3141b"/>
    <polygon points="205,77 244,77 240,84 201,84" fill="#4a4a4a"/>
    <polygon points="30,77 60,77 56,84 26,84" fill="#4a4a4a"/>
    <polygon points="63,77 118,77 114,84 59,84" fill="#d3141b"/>
    <polygon points="121,77 162,77 158,84 117,84" fill="#4a4a4a"/>
    <polygon points="165,77 207,77 203,84 161,84" fill="#d3141b"/>
    <polygon points="210,77 245,77 241,84 206,84" fill="#4a4a4a"/>
    <g fill="#fff"><text x="48" y="82.5">1990</text><text x="90" y="82.5">2001</text><text x="138" y="82.5">2007</text><text x="184" y="82.5">2012</text><text x="226" y="82.5">2020</text></g>
    <g stroke="#222" stroke-width=".8"><line x1="48" y1="66" x2="48" y2="77"/><line x1="138" y1="66" x2="138" y2="77"/><line x1="226" y1="66" x2="226" y2="77"/><line x1="92" y1="84" x2="92" y2="95"/><line x1="184" y1="84" x2="184" y2="95"/></g>
    <g fill="#222"><circle cx="48" cy="66" r="1.2"/><circle cx="138" cy="66" r="1.2"/><circle cx="226" cy="66" r="1.2"/><circle cx="92" cy="95" r="1.2"/><circle cx="184" cy="95" r="1.2"/></g>
    <g font-size="4.2"><text x="48" y="48">Your Title</text><text x="138" y="48">Your Title</text><text x="226" y="48">Your Title</text><text x="92" y="104">Your Title</text><text x="184" y="104">Your Title</text></g>
    <g font-size="3.2" font-weight="400" fill="#777"><text x="48" y="53">Refers to a good or</text><text x="48" y="57">service being offered</text><text x="138" y="53">Refers to a good or</text><text x="138" y="57">service being offered</text><text x="226" y="53">Refers to a good or</text><text x="226" y="57">service being offered</text><text x="92" y="109">Refers to a good or</text><text x="92" y="113">service being offered</text><text x="184" y="109">Refers to a good or</text><text x="184" y="113">service being offered</text></g>
  </svg>
  <div class="foot"><span>15</span></div>
</section>

<section class="slide c2 r6">
  <div class="title">Text Added Hare</div><div class="brand"><i></i>Marlow Pike</div>
  <svg class="abs" style="left:0;top:0" width="270" height="152">
    <g transform="translate(136,78)" fill="none" stroke-width="16">
      <circle r="28" stroke="#4a4a4a" stroke-dasharray="42 176" transform="rotate(1)"/>
      <circle r="28" stroke="#d3141b" stroke-dasharray="42 176" transform="rotate(91)"/>
      <circle r="28" stroke="#4a4a4a" stroke-dasharray="42 176" transform="rotate(181)"/>
      <circle r="28" stroke="#d3141b" stroke-dasharray="42 176" transform="rotate(271)"/>
    </g>
    <g fill="#fff"><circle cx="124" cy="58" r="3"/><circle cx="152" cy="62" r="3"/><circle cx="120" cy="94" r="3"/><circle cx="155" cy="93" r="3"/></g>
    <text x="136" y="77" text-anchor="middle" font-family="Montserrat" font-size="6" font-weight="700" fill="#222">Text</text>
    <text x="136" y="84" text-anchor="middle" font-family="Montserrat" font-size="6" font-weight="700" fill="#222">Added</text>
  </svg>
  <div class="abs" style="left:26px;top:39px;width:72px;text-align:right"><div class="h6">Text Here</div><div class="fine" style="margin-top:1px">Short note describing this quarter of the cycle.</div></div>
  <div class="abs" style="left:26px;top:95px;width:72px;text-align:right"><div class="h6">Text Here</div><div class="fine" style="margin-top:1px">Short note describing this quarter of the cycle.</div></div>
  <div class="abs" style="left:180px;top:39px;width:72px"><div class="h6">Text Here</div><div class="fine" style="margin-top:1px">Short note describing this quarter of the cycle.</div></div>
  <div class="abs" style="left:180px;top:95px;width:72px"><div class="h6">Text Here</div><div class="fine" style="margin-top:1px">Short note describing this quarter of the cycle.</div></div>
  <div class="foot"><span>15</span></div>
</section>

<section class="slide c3 r6">
  <div class="title">Text Added Hare</div><div class="brand"><i></i>Marlow Pike</div>
  <svg class="abs" style="left:0;top:0" width="270" height="152" font-family="Montserrat" font-size="3.2" font-weight="600" text-anchor="middle">
    <rect x="20" y="73" width="226" height="3" fill="#4a4a4a"/>
    <rect x="115" y="73" width="131" height="3" fill="#d3141b"/>
    <path d="M246 70l6 4.5-6 4.5z" fill="#d3141b"/>
    <g fill="none" stroke-width="5">
      <circle cx="65" cy="60" r="13" stroke="#4a4a4a"/><circle cx="112" cy="60" r="13" stroke="#d3141b"/>
      <circle cx="160" cy="60" r="13" stroke="#4a4a4a"/><circle cx="207" cy="60" r="13" stroke="#d3141b"/>
    </g>
    <g fill="none" stroke="#222" stroke-width=".8">
      <circle cx="65" cy="60" r="5"/><path d="M65 57v3h2.5"/>
      <circle cx="112" cy="60" r="5" fill="#222"/>
      <ellipse cx="160" cy="57" rx="4" ry="1.5"/><path d="M156 57v5c0 1 8 1 8 0v-5"/>
      <circle cx="206" cy="59" r="3.5"/><path d="M209 62l3 3"/>
    </g>
    <g fill="#fff"><text x="65" y="75.6">Step 01</text><text x="112" y="75.6">Step 02</text><text x="160" y="75.6">Step 03</text><text x="215" y="75.6">Step 04</text></g>
    <g font-size="5" fill="#222"><text x="65" y="92">Lorem Ipsum</text><text x="112" y="92">Lorem Ipsum</text><text x="160" y="92">Lorem Ipsum</text><text x="207" y="92">Lorem Ipsum</text></g>
  </svg>
  <div class="abs fine" style="left:45px;top:95px;width:40px;text-align:center;font-size:2.8px">Short note on this stage of the plan.</div>
  <div class="abs fine" style="left:92px;top:95px;width:40px;text-align:center;font-size:2.8px">Short note on this stage of the plan.</div>
  <div class="abs fine" style="left:140px;top:95px;width:40px;text-align:center;font-size:2.8px">Short note on this stage of the plan.</div>
  <div class="abs fine" style="left:187px;top:95px;width:40px;text-align:center;font-size:2.8px">Short note on this stage of the plan.</div>
  <div class="foot"><span>16</span></div>
</section>

<!-- Row 7 -->
<section class="slide c1 r7">
  <div class="title">Text Added Hare</div><div class="brand"><i></i>Marlow Pike</div>
  <div class="abs fine" style="left:15px;top:31px;width:85px">A short paragraph introducing the digital service and how it supports each stage of the client journey.<br><br>A second short paragraph adding supporting detail.</div>
  <div class="abs" style="left:15px;top:78px;width:85px">
    <div style="display:flex;gap:4px;margin-bottom:8px"><span style="background:var(--red);color:#fff;font-size:4px;font-weight:700;width:7px;height:7px;text-align:center">1.</span><div><div class="h6" style="font-size:3.8px">Lorem ipsum</div><div class="fine" style="font-size:2.8px">Short supporting line here.</div></div></div>
    <div style="display:flex;gap:4px;margin-bottom:8px"><span style="background:var(--red);color:#fff;font-size:4px;font-weight:700;width:7px;height:7px;text-align:center">2.</span><div><div class="h6" style="font-size:3.8px">Lorem ipsum</div><div class="fine" style="font-size:2.8px">Short supporting line here.</div></div></div>
    <div style="display:flex;gap:4px"><span style="background:var(--red);color:#fff;font-size:4px;font-weight:700;width:7px;height:7px;text-align:center">3.</span><div><div class="h6" style="font-size:3.8px">Lorem ipsum</div><div class="fine" style="font-size:2.8px">Short supporting line here.</div></div></div>
  </div>
  <div class="abs" style="left:133px;top:21px;width:32px;height:67px;border:1.5px solid #333;border-radius:4px;padding:12px 3px 0"><div style="font-size:3.8px;line-height:1.2">Lorem<br>ipsum dolor</div><div style="width:8px;height:6px;border:.8px solid var(--red);margin:4px 0"></div><div class="fine" style="font-size:2.4px">Short screen copy here.</div></div>
  <div class="abs" style="left:174px;top:41px;width:32px;height:67px;border:1.5px solid #333;border-radius:4px;padding:12px 3px 0"><div style="font-size:3.8px;line-height:1.2">Dolor sit<br>amet, conse</div><div style="width:8px;height:6px;border:.8px solid var(--red);margin:4px 0"></div><div class="fine" style="font-size:2.4px">Short screen copy here.</div></div>
  <div class="abs" style="left:214px;top:62px;width:32px;height:67px;border:1.5px solid #333;border-radius:4px;padding:12px 3px 0"><div style="font-size:3.8px;line-height:1.2">Consec</div><div style="width:7px;height:7px;border:.8px solid var(--red);border-radius:50%;margin:5px 0 4px 8px"></div><div class="fine" style="font-size:2.4px">Short screen copy here.</div></div>
  <div class="foot"><span>17</span></div>
</section>

<section class="slide c2 r7">
  <div class="title">Text Added Hare</div><div class="brand"><i></i>Marlow Pike</div>
  <div class="abs" style="left:24px;top:48px;width:222px;display:flex;gap:12px">
    <div style="flex:1;text-align:center;position:relative"><div style="height:14px;background:#4a4a4a"></div><div role="img" aria-label="Team member portrait" style="width:20px;height:20px;border-radius:50%;background:linear-gradient(135deg,#bbb,#888);border:1.5px solid #fff;margin:-9px auto 3px;position:relative"></div><div style="font-size:4.5px;font-weight:600">THEO BRANDT</div><div class="fine" style="font-size:2.6px;margin-top:2px">Short bio line about role and focus.</div></div>
    <div style="flex:1;text-align:center;position:relative"><div style="height:14px;background:var(--red)"></div><div role="img" aria-label="Team member portrait" style="width:20px;height:20px;border-radius:50%;background:linear-gradient(135deg,#bbb,#888);border:1.5px solid #fff;margin:-9px auto 3px;position:relative"></div><div style="font-size:4.5px;font-weight:600">INES VARGA</div><div class="fine" style="font-size:2.6px;margin-top:2px">Short bio line about role and focus.</div></div>
    <div style="flex:1;text-align:center;position:relative"><div style="height:14px;background:#4a4a4a"></div><div role="img" aria-label="Team member portrait" style="width:20px;height:20px;border-radius:50%;background:linear-gradient(135deg,#bbb,#888);border:1.5px solid #fff;margin:-9px auto 3px;position:relative"></div><div style="font-size:4.5px;font-weight:600">THEO BRANDT</div><div class="fine" style="font-size:2.6px;margin-top:2px">Short bio line about role and focus.</div></div>
    <div style="flex:1;text-align:center;position:relative"><div style="height:14px;background:var(--red)"></div><div role="img" aria-label="Team member portrait" style="width:20px;height:20px;border-radius:50%;background:linear-gradient(135deg,#bbb,#888);border:1.5px solid #fff;margin:-9px auto 3px;position:relative"></div><div style="font-size:4.5px;font-weight:600">INES VARGA</div><div class="fine" style="font-size:2.6px;margin-top:2px">Short bio line about role and focus.</div></div>
  </div>
  <div class="foot"><span>17</span></div>
</section>

<section class="slide c3 r7">
  <div class="abs" style="left:88px;top:26px;font-size:19px;font-weight:800">Thank You</div>
  <div class="abs" style="left:112px;top:70px;width:158px;height:67px;background:linear-gradient(90deg,#8a8a8a,#6c6c6c)"></div>
  <div class="abs" style="left:110px;top:96px;width:20px;height:20px;border-radius:50%;background:var(--red)"></div>
  <svg class="abs" style="left:178px;top:79px" width="8" height="54" fill="#fff">
    <path d="M1 1h2l1 2-1 1c.5 1 1.5 2 2.5 2.5l1-1 2 1v2c-4 0-7.5-3.5-7.5-7.5z"/>
    <path d="M1 22l6-3-2 6-1-2z"/>
    <path d="M4 40l-3.5 3h1v3h5v-3h1z"/>
  </svg>
  <div class="abs" style="left:194px;top:78px;color:#fff;font-size:4px;line-height:1.3">
    <div>+1 555 0142 7788<br>+1 555 0142 7788</div>
    <div style="margin-top:9px">www.marlowpike-demo.com<br>hello@marlowpike-demo.com</div>
    <div style="margin-top:9px">1234 Street name, town/city,<br>state/country, post/zip 012345.</div>
  </div>
</section>

</body>
</html>
```